Political sign design, fonts colors and layout

I am running for Town Council.

My message is done, and *a draft is attached* with the text we wish to use. It says "Elect Dana Velmont" etc. In Maroon and White. I am not a designer, but this is somewhat close to what we are looking for.

I need help with colors and fonts, layout, spacing, and general cleanup.

I'm attaching the town high school logo:

- "H" for Brookfield: with black and white outlines on the fonts
- we want to incorporate the black and white on the fonts
- for the entire text, parts of the text, or best would be a mix

This is for signs printed and placed all over my town.

We need two versions

1. square, 4' by 4' version
2. 36" by 24" version

The smaller version will drop the three bullet pointed text, but otherwise can be identical.

The sign can only use 3 printed colors (due to printing costs.)

1. maroon,
2. white,
3. black.

The maroon should match the maroon from the high school logo attached, which I believe I did in the draft.

We also like the white border around the outside, like in the "scoreboard" design attached.

Thanks for your attention, wish me luck.

Dana

Target Market(s)

SIgns, Political market

Industry/Entity Type

Political

Font styles to use
Sans Serif
Other font styles liked:
• Arial Black, Sans Serif Bold

Requirements
Must have
• maroon background, white font.
• - black borders around fonts where appropriate
• - great spacing
• - great typeface usage
• - clean and crisp political sign, visible while driving.
• - my name "Dana Velmont" much larger like the draft, or the appropriate additional size
• - two versions, one square, and one 36" / 24"
Nice to have
• - nice borders
• - dress it up a bit, using italics and bold fonts, without making it flashy or busy.
Should not have
• Must be easily readable from a car, except for "Paid for by Friends of Dana Velmont" which can be tiny.
• Colors are noted in the description, the "Brookfield Maroon" as the background, white font, and some use of black.

```html
<!DOCTYPE html>
<html lang="en">
<head>
<meta charset="utf-8">
<title>Elect Dana Velmont – Yard Sign</title>
<link rel="stylesheet" href="https://fonts.googleapis.com/css2?family=Archivo+Black&family=Arimo:ital,wght@0,700;1,400;1,700&family=Open+Sans:wght@700;800&display=swap">
<style>
  :root {
    --maroon: #843243;
    --white: #ffffff;
    --black: #000000;
  }
  html, body {
    margin: 0;
    padding: 0;
    width: 1200px;
    height: 1017px;
    overflow: hidden;
    background: var(--white);
  }
  .sign { display: block; width: 1200px; height: 1017px; }
  .fill-maroon { fill: var(--maroon); }
  .fill-white { fill: var(--white); }
  .fill-black { fill: var(--black); }

  .headline {
    font-family: "Open Sans", sans-serif;
    font-weight: 800;
    font-size: 60px;
    fill: var(--white);
  }
  .elect {
    font-family: "Open Sans", sans-serif;
    font-weight: 800;
    font-size: 56px;
    fill: var(--black);
  }
  .candidate-name {
    font-family: "Archivo Black", sans-serif;
    font-size: 122px;
    fill: var(--maroon);
    stroke-linejoin: round;
  }
  .candidate-name.outline-black { stroke: var(--black); stroke-width: 16px; }
  .candidate-name.outline-white { stroke: var(--white); stroke-width: 7px; }
  .office {
    font-family: "Arimo", sans-serif;
    font-style: italic;
    font-size: 29px;
    letter-spacing: 1px;
    fill: var(--black);
  }
  .tagline {
    font-family: "Arimo", sans-serif;
    font-style: italic;
    font-size: 42px;
    fill: var(--white);
  }
  .tagline .strong { font-weight: 700; }
  .tagline .underline { text-decoration: underline; }
  .website {
    font-family: "Open Sans", sans-serif;
    font-weight: 800;
    font-size: 56px;
    letter-spacing: 5px;
    fill: var(--white);
  }
  .platform {
    font-family: "Arimo", sans-serif;
    font-weight: 700;
    font-size: 27px;
    fill: var(--white);
  }
  .vote-call {
    font-family: "Open Sans", sans-serif;
    font-weight: 800;
    font-size: 66px;
    fill: var(--maroon);
  }
  .disclaimer {
    font-family: "Arimo", sans-serif;
    font-weight: 700;
    font-size: 20px;
    fill: var(--black);
  }
</style>
</head>
<body>
<svg class="sign" viewBox="0 0 1400 1187" xmlns="http://www.w3.org/2000/svg" role="img" aria-label="Campaign sign: Elect Dana Velmont for Brookfield Councilman/Trustee">
  <!-- sign frame -->
  <rect class="fill-maroon" x="93" y="188" width="1213" height="809"/>
  <rect class="fill-white" x="101" y="197" width="1197" height="791"/>
  <rect class="fill-maroon" x="116" y="214" width="1168" height="758"/>

  <!-- headline -->
  <text class="headline" x="709" y="295" text-anchor="middle">Take back our Town!</text>

  <!-- name panel -->
  <rect class="fill-white" x="139" y="325" width="1122" height="195"/>
  <text class="elect" x="170" y="414">Elect</text>
  <text class="candidate-name outline-black" x="334" y="443" textLength="884" lengthAdjust="spacingAndGlyphs">DANA VELMONT</text>
  <text class="candidate-name outline-white" x="334" y="443" textLength="884" lengthAdjust="spacingAndGlyphs">DANA VELMONT</text>
  <text class="candidate-name" x="334" y="443" textLength="884" lengthAdjust="spacingAndGlyphs">DANA VELMONT</text>
  <text class="office" x="1220" y="493" text-anchor="end">for Brookfield Councilman/Trustee</text>

  <!-- tagline -->
  <text class="tagline" x="707" y="583" text-anchor="middle"><tspan class="strong underline">Fighting</tspan> for <tspan class="strong">Brookfield</tspan></text>

  <!-- website band -->
  <rect class="fill-black" x="127" y="615" width="1146" height="77"/>
  <text class="website" x="697" y="672" text-anchor="middle">www.votevelmont.com</text>

  <!-- platform -->
  <text class="platform" x="690" y="728" text-anchor="middle">Stop HiGH taxes</text>
  <text class="platform" x="690" y="768" text-anchor="middle">Clean up our government</text>
  <text class="platform" x="690" y="808" text-anchor="middle">Preserve our Neighborhoods</text>

  <!-- vote tab -->
  <polygon class="fill-white" points="240,972 323,833 1078,833 1160,972"/>
  <text class="vote-call" x="707" y="929" text-anchor="middle">Vote Nov. 8th “Row A”</text>
  <text class="disclaimer" x="318" y="968">Paid for by Friends of Dana</text>
</svg>
</body>
</html>
```